Visitenkarten-Design für App Start Up
Zielgruppe
Wir sind ein Start-Up und haben unsere Murento App gerelauncht.
Wir haben zwei Zielgruppen für unsere App. Zum einen lokale Gewerbetreibende, welche in Echtzeit Angebote (Coupons) erstellen können und zum anderen private User, welche diese innerhalb eines vorgegebenen Zeitraumes reservieren und einlösen können.
Hierfür müssen wir auch unsere Visitenkarten auf unser neues Design anpassen.
Aufgabenstellung
Visitenkarten sollten beidseitig bedruckt sein und auf der Vorderseite sollte unser Murento Logo und/oder der App Name Murento versehen sein. Auf der Rückseite benötigen wir die Infos: Name, Position, Firma inkl. Anschrift, E-Mail sowie die Telefonnummer.
Ansonsten freuen wir uns auf weitere kreative Ansätze.

```html
<!DOCTYPE html>
<html lang="de">
<head>
<meta charset="utf-8">
<title>Murento – Visitenkarten</title>
<link rel="stylesheet" href="https://fonts.googleapis.com/css2?family=Open+Sans:wght@400;600;700&display=swap">
<style>
  :root {
    --bg: #1c1c1e;
    --card-light: #ffffff;
    --card-dark: #2a2a2c;
    --card-dark-edge: #1f1f21;
    --ink: #1d1d1f;
    --ink-soft: #555a60;
    --accent-blue: #1a7fd0;
    --accent-pink: #d7338f;
    --divider: #9a9ea3;
    --on-dark: #f2f2f2;
  }
  * { box-sizing: border-box; margin: 0; padding: 0; }
  html, body { width: 1200px; height: 900px; overflow: hidden; }
  body {
    background: var(--bg);
    font-family: "Open Sans", Arial, sans-serif;
    position: relative;
  }
  .card {
    position: absolute;
    left: 320px;
    width: 560px;
    height: 320px;
    border-radius: 4px;
    box-shadow: 0 18px 40px rgba(0,0,0,.5);
  }
  .card--front { top: 100px; background: var(--card-light); }
  .card--back {
    top: 470px;
    background: linear-gradient(150deg, #303033 0%, var(--card-dark) 50%, var(--card-dark-edge) 100%);
  }

  .brand {
    position: absolute;
    display: flex;
    align-items: center;
    gap: 12px;
  }
  .brand__mark { width: 16px; height: 16px; background: var(--accent-blue); }
  .brand__name {
    font-weight: 600;
    letter-spacing: .28em;
    text-transform: uppercase;
  }
  .card--front .brand { left: 52px; top: 178px; }
  .card--front .brand__name { font-size: 26px; color: var(--ink); }
  .card--back .brand { right: 44px; bottom: 118px; }
  .card--back .brand__mark { width: 12px; height: 12px; }
  .card--back .brand__name { font-size: 16px; color: var(--on-dark); }

  .divider {
    position: absolute;
    left: 262px; top: 92px;
    width: 1px; height: 118px;
    background: var(--divider);
  }

  .contact { position: absolute; left: 284px; top: 88px; }
  .contact__name { font-size: 18px; font-weight: 700; color: var(--ink-soft); letter-spacing: .02em; }
  .contact__name .first { color: var(--accent-blue); }
  .contact__role { font-size: 11px; font-weight: 600; color: var(--ink-soft); margin: 1px 0 8px; letter-spacing: .04em; }
  .contact__list { list-style: none; }
  .contact__list li {
    display: flex; align-items: center; gap: 9px;
    font-size: 12.5px; color: var(--ink); line-height: 19px;
  }
  .contact__list svg { width: 11px; height: 11px; fill: var(--accent-blue); flex: none; }
</style>
</head>
<body>

<section class="card card--front" aria-label="Visitenkarte Vorderseite">
  <div class="brand">
    <span class="brand__mark"></span>
    <span class="brand__name">Murento</span>
  </div>
  <div class="divider"></div>
  <div class="contact">
    <p class="contact__name"><span class="first">TOMAS</span> BELWICK</p>
    <p class="contact__role">Director</p>
    <ul class="contact__list">
      <li><svg viewBox="0 0 24 24"><path d="M6.6 10.8a15 15 0 0 0 6.6 6.6l2.2-2.2a1 1 0 0 1 1-.25 11.4 11.4 0 0 0 3.6.57 1 1 0 0 1 1 1V20a1 1 0 0 1-1 1A17 17 0 0 1 3 4a1 1 0 0 1 1-1h3.5a1 1 0 0 1 1 1c0 1.25.2 2.45.57 3.57a1 1 0 0 1-.25 1z"/></svg>555-014-2291</li>
      <li><svg viewBox="0 0 24 24"><path d="M2 5h20v14H2zm2 2v.5l8 5 8-5V7l-8 5z"/></svg>tbelwick@harlowden.com</li>
      <li><svg viewBox="0 0 24 24"><path d="M12 2a10 10 0 1 0 0 20 10 10 0 0 0 0-20zm6.9 6h-3a15 15 0 0 0-1.3-3.9A8 8 0 0 1 18.9 8zM12 4c.8 1.2 1.5 2.5 1.9 4h-3.8c.4-1.5 1.1-2.8 1.9-4zM4.3 14a8 8 0 0 1 0-4h3.4a16 16 0 0 0 0 4zm.8 2h3a15 15 0 0 0 1.3 3.9A8 8 0 0 1 5.1 16zm3-8h-3a8 8 0 0 1 4.3-3.9A15 15 0 0 0 8.1 8zM12 20c-.8-1.2-1.5-2.5-1.9-4h3.8c-.4 1.5-1.1 2.8-1.9 4zm2.3-6H9.7a14 14 0 0 1 0-4h4.6a14 14 0 0 1 0 4zm.3 5.9a15 15 0 0 0 1.3-3.9h3a8 8 0 0 1-4.3 3.9zm1.7-5.9a16 16 0 0 0 0-4h3.4a8 8 0 0 1 0 4z"/></svg>www.harlowden.com</li>
      <li><svg viewBox="0 0 24 24"><path d="M12 2a7 7 0 0 0-7 7c0 5.2 7 13 7 13s7-7.8 7-13a7 7 0 0 0-7-7zm0 9.5A2.5 2.5 0 1 1 12 6.5a2.5 2.5 0 0 1 0 5z"/></svg>48 Elm Lane, CT 06012</li>
    </ul>
  </div>
</section>

<section class="card card--back" aria-label="Visitenkarte Rückseite">
  <div class="brand">
    <span class="brand__mark"></span>
    <span class="brand__name">Murento</span>
  </div>
</section>

</body>
</html>
```